Super-fantastic-interesting infographic of terribly boring content

-Looking to provide a visually engaging snapshot of the average Canadian investor.
-Help people compare their personal financial situation against the infographic (Average).
-We want viewers to feel engaged and interested in the info presented, not confused and irritated.

Data points to present:

The average Canadian snapshot:
* Average Canadian household Income in 2016: $76,900
* Median Net Worth of Canadian families in 2016: $295,100
* Average annual household expenditures on goods a& services: $62,183
* Median value in principal residence: $349,000
* Highest net annual savings amount (Age 35-44): $10,120
* Number of Canadian families holding a mortgage: 38.4%
* Median Mortgage value of Principal residence: $190,000
* Debt to disposable income ratio average: 172.1
* Total value of all assets held by Canadians in 2016: 12 Trillion dollars
* The principal residence was the single largest asset held (of the 12 Trillion): 32%
* Private pensions was the 2nd largest grouping of assets at 29.2%
* The average borrowing rate for Canadian mortgages: 2.94%
* 74% were fixed rate, 21% were variable and 5% blended.
* 48% of Canadians do not save or invest at all
* 54% of Canadians do not budget regularly
* 1 in 3 Canadians have lost at least 20% in one year
* 51% of Canadians took NO ACTION after losing at least 20% in one year.
* 22% of those people either, hired or fired an advisor

Financial advice landscape:
* # of households in Canada: 13,300,000
* Households with an advisor 5,300,000
* % of households dissatisfied with existing advisor 1,100,000

Target Market(s)

Investors, ages 22-55

Industry/Entity Type

Financial

Font styles to use
Sans Serif

Colors

Designer to choose colors to be used in the design.

Requirements
Must have
• Header: Financial landscape of the average Canadian
Nice to have
• There is a lot of numbers and percentages, find a way to deliver the info using a mix of images, numbers, pictures etc.

```html
<!DOCTYPE html>
<html lang="en">
<head>
<meta charset="utf-8">
<title>Financial Landscape of the Average Canadian</title>
<link rel="stylesheet" href="https://fonts.googleapis.com/css2?family=Nunito:wght@300;400;800;900&family=Nunito+Sans:wght@400;600&display=swap">
<style>
  :root {
    --panel: #34748f;
    --panel-dark: #1f4d63;
    --teal: #5ccadb;
    --teal-soft: #72d0e0;
    --orange: #f6a834;
    --green: #8cc63f;
    --white: #ffffff;
    --shadow: #e6e6e8;
    --ink: #1d4356;
  }
  * { box-sizing: border-box; margin: 0; padding: 0; }
  html, body { width: 1200px; height: 1200px; overflow: hidden; background: var(--white); }
  .canvas { position: relative; width: 1200px; height: 1200px; font-family: "Nunito Sans", sans-serif; color: var(--white); }
  .backdrop { position: absolute; left: 42px; top: 154px; width: 1140px; height: 864px; background: var(--shadow); }
  .panel { position: absolute; left: 30px; top: 167px; width: 1140px; height: 865px; background: var(--panel); }
  .abs { position: absolute; }

  .brand-tab-shadow { left: 230px; top: 167px; width: 194px; height: 92px; background: var(--panel-dark); border-radius: 0 0 6px 6px; }
  .brand-tab { left: 238px; top: 167px; width: 180px; height: 89px; background: var(--white); border-radius: 0 0 6px 6px;
    display: flex; align-items: center; justify-content: center; gap: 7px; }
  .brand-dot { width: 26px; height: 26px; border-radius: 50%; background: var(--panel); }
  .brand-name { font-family: "Nunito", sans-serif; font-weight: 800; font-size: 20px; color: var(--panel); }

  .title-small { left: 442px; top: 180px; font-family: "Nunito", sans-serif; font-weight: 300; font-size: 25px; letter-spacing: 1.5px; }
  .title-big { left: 440px; top: 202px; font-family: "Nunito", sans-serif; font-weight: 900; font-size: 52px; letter-spacing: -1px;
    color: var(--teal); text-shadow: 3px 3px 0 var(--panel-dark); white-space: nowrap; }

  .rule { left: 69px; width: 1062px; height: 3px; background: var(--white); }
  .rule-top { top: 271px; }
  .rule-bottom { top: 1013px; }

  .section-label { left: 69px; width: 412px; height: 32px; background: var(--panel-dark);
    font-family: "Nunito", sans-serif; font-weight: 900; font-size: 22px; padding-left: 22px; line-height: 32px; }

  .stat { font-size: 14.5px; line-height: 16.5px; }
  .stat .value { font-family: "Nunito", sans-serif; font-weight: 900; font-size: 30px; line-height: 36px; color: var(--teal); letter-spacing: -0.3px; }
  .stat .value.wide { font-size: 29px; }
  .stat .lead { font-family: "Nunito", sans-serif; font-weight: 900; font-size: 30px; line-height: 34px; color: var(--teal); margin-bottom: 1px; }
  .stat em { font-style: normal; font-weight: 600; color: var(--teal); }
  .stat .value.orange { color: var(--orange); }

  .col-1 { left: 181px; }
  .col-2 { left: 555px; }
  .col-3 { left: 918px; }

  .icon-fill { background: var(--teal-soft); border-radius: 4px; }
  .icon-fill.orange { background: var(--orange); }
  .icon-fill.pale { background: var(--white); opacity: 0.9; }
</style>
</head>
<body>
<div class="canvas">
  <div class="backdrop"></div>
  <div class="panel"></div>

  <div class="abs brand-tab-shadow"></div>
  <div class="abs brand-tab"><span class="brand-dot"></span><span class="brand-name">LedgerMark</span></div>

  <div class="abs title-small">FINANCIAL LANDSCAPE OF</div>
  <h1 class="abs title-big">THE AVERAGE CANADIAN</h1>
  <div class="abs rule rule-top"></div>

  <h2 class="abs section-label" style="top:285px">The average Canadian snapshot:</h2>

  <!-- Column one icons -->
  <svg class="abs" style="left:72px;top:338px" width="100" height="400" viewBox="0 0 100 400" aria-hidden="true">
    <g font-family="Nunito, sans-serif" font-weight="900" font-size="26" fill="var(--ink)" text-anchor="middle">
      <g transform="translate(25,30)"><circle r="21" fill="#fff" stroke="var(--teal-soft)" stroke-width="4"/><text y="9">$</text></g>
      <g transform="translate(25,119)"><circle r="21" fill="#fff" stroke="var(--teal-soft)" stroke-width="4"/><text y="9">$</text></g>
      <g transform="translate(25,206)"><circle r="21" fill="#fff" stroke="var(--teal-soft)" stroke-width="4"/><text y="9">$</text></g>
      <g transform="translate(25,291)"><circle r="21" fill="#fff" stroke="var(--teal-soft)" stroke-width="4"/><text y="9">$</text></g>
      <g transform="translate(25,373)"><circle r="21" fill="#fff" stroke="var(--teal-soft)" stroke-width="4"/><text y="9">$</text></g>
    </g>
  </svg>
  <div class="abs icon-fill" style="left:108px;top:342px;width:54px;height:50px" role="img" aria-label="House icon"></div>
  <div class="abs icon-fill" style="left:106px;top:424px;width:60px;height:64px" role="img" aria-label="Family icon"></div>
  <div class="abs icon-fill" style="left:104px;top:510px;width:62px;height:64px" role="img" aria-label="Gear and wrench icon"></div>
  <div class="abs icon-fill" style="left:106px;top:597px;width:58px;height:62px" role="img" aria-label="Apartment building icon"></div>
  <div class="abs icon-fill" style="left:108px;top:680px;width:58px;height:60px" role="img" aria-label="Hand holding coin icon"></div>

  <!-- Donut charts -->
  <svg class="abs" style="left:0;top:0" width="1200" height="1200" viewBox="0 0 1200 1200" aria-hidden="true">
    <defs>
      <g id="ring-base"><circle r="36" fill="var(--white)"/><circle r="30" fill="var(--panel)"/><circle r="23" fill="var(--panel-dark)"/></g>
    </defs>
    <g font-family="Nunito, sans-serif" font-weight="900" font-size="20" fill="var(--teal-soft)" text-anchor="middle">
      <!-- 38.4% -->
      <g transform="translate(118,793)"><use href="#ring-base"/><circle r="33" fill="none" stroke="var(--orange)" stroke-width="6" stroke-dasharray="79.6 207.3" transform="rotate(-90)" pathLength="207.3"/><circle r="23" fill="var(--panel-dark)"/><text y="7">%</text></g>
      <!-- 32% -->
      <g transform="translate(490,636)"><use href="#ring-base"/><circle r="33" fill="none" stroke="var(--orange)" stroke-width="6" stroke-dasharray="66.3 207.3" transform="rotate(-90)"/></g>
      <!-- 29.2% -->
      <g transform="translate(490,724)"><use href="#ring-base"/><circle r="33" fill="none" stroke="var(--orange)" stroke-width="6" stroke-dasharray="60.5 207.3" transform="rotate(-90)"/></g>
      <!-- 2.94% -->
      <g transform="translate(490,810)"><use href="#ring-base"/><circle r="33" fill="none" stroke="var(--orange)" stroke-width="6" stroke-dasharray="6.1 207.3" transform="rotate(-90)"/><text y="7">%</text></g>
      <!-- 74/21/5 -->
      <g transform="translate(858,358)"><circle r="36" fill="var(--white)"/>
        <circle r="33" fill="none" stroke="var(--orange)" stroke-width="7" stroke-dasharray="153.4 207.3" transform="rotate(-8)"/>
        <circle r="33" fill="none" stroke="var(--green)" stroke-width="7" stroke-dasharray="43.5 207.3" transform="rotate(-134)"/>
        <circle r="33" fill="none" stroke="#b9b9b9" stroke-width="7" stroke-dasharray="10.4 207.3" transform="rotate(-90)"/>
        <circle r="27" fill="var(--panel)"/><circle r="21" fill="var(--panel-dark)"/><text y="7">%</text></g>
      <!-- 48% -->
      <g transform="translate(858,442)"><use href="#ring-base"/><circle r="33" fill="none" stroke="var(--orange)" stroke-width="6" stroke-dasharray="99.5 207.3" transform="rotate(-90)"/></g>
      <!-- 54% -->
      <g transform="translate(858,524)"><use href="#ring-base"/><circle r="33" fill="none" stroke="var(--orange)" stroke-width="6" stroke-dasharray="111.9 207.3" transform="rotate(-90)"/></g>
      <!-- 51% -->
      <g transform="translate(858,714)"><use href="#ring-base"/><circle r="33" fill="none" stroke="var(--orange)" stroke-width="6" stroke-dasharray="105.7 207.3" transform="rotate(-90)"/></g>
      <!-- 22% -->
      <g transform="translate(858,810)"><use href="#ring-base"/><circle r="33" fill="none" stroke="var(--orange)" stroke-width="6" stroke-dasharray="45.6 207.3" transform="rotate(-90)"/></g>
    </g>
    <!-- debt pie -->
    <g transform="translate(490,456)">
      <path d="M4,-4 L4,-32 A30,30 0 1 1 -22,18 Z" fill="var(--teal-soft)"/>
      <path d="M-4,-4 L-30,6 A30,30 0 0 1 -4,-32 Z" fill="none" stroke="var(--white)" stroke-width="3"/>
    </g>
  </svg>
  <div class="abs icon-fill pale" style="left:852px;top:430px;width:14px;height:18px;border-radius:50%;opacity:0.25" role="img" aria-label="Coin in hand with cross icon"></div>
  <div class="abs icon-fill pale" style="left:849px;top:511px;width:18px;height:24px;opacity:0.3" role="img" aria-label="Calculator with cross icon"></div>
  <div class="abs icon-fill pale" style="left:849px;top:700px;width:18px;height:26px;opacity:0.3" role="img" aria-label="Person sitting on a box icon"></div>
  <div class="abs icon-fill pale" style="left:844px;top:797px;width:28px;height:26px;opacity:0.3" role="img" aria-label="Two people pointing icon"></div>
  <div class="abs icon-fill pale" style="left:478px;top:624px;width:24px;height:24px;opacity:0.3" role="img" aria-label="Building icon"></div>
  <div class="abs icon-fill pale" style="left:476px;top:712px;width:28px;height:24px;opacity:0.3" role="img" aria-label="Group of people icon"></div>

  <!-- Column two icons -->
  <svg class="abs" style="left:444px;top:338px" width="40" height="40" viewBox="0 0 40 40" aria-hidden="true">
    <circle cx="20" cy="20" r="17" fill="#fff" stroke="var(--teal-soft)" stroke-width="4"/>
    <text x="20" y="28" font-family="Nunito, sans-serif" font-weight="900" font-size="22" fill="var(--ink)" text-anchor="middle">%</text>
  </svg>
  <div class="abs icon-fill" style="left:480px;top:336px;width:54px;height:62px" role="img" aria-label="Office building icon"></div>
  <div class="abs icon-fill" style="left:438px;top:522px;width:106px;height:38px" role="img" aria-label="Row of houses icon"></div>

  <!-- Column three people -->
  <div class="abs icon-fill" style="left:806px;top:592px;width:102px;height:46px;background:linear-gradient(90deg,#fff 0 62%,var(--teal-soft) 62%)" role="img" aria-label="Three people icon, one highlighted"></div>

  <!-- Column one stats -->
  <div class="abs stat col-1" style="top:334px">Average Canadian<br>household Income in 2016<div class="value">$76,900</div></div>
  <div class="abs stat col-1" style="top:422px">Median Net Worth<br>of Canadian families in 2016<div class="value">$295,100</div></div>
  <div class="abs stat col-1" style="top:510px">Average annual household<br>expenditures on goods a&amp; services<div class="value">$62,183</div></div>
  <div class="abs stat col-1" style="top:595px">Median value<br>in principal residence<div class="value">$349,000</div></div>
  <div class="abs stat col-1" style="top:677px">Highest net annual<br>savings amount (Age 35-44)<div class="value">$10,120</div></div>
  <div class="abs stat col-1" style="top:762px">Number of Canadian families<br>holding a mortgage<div class="value">38.4%</div></div>

  <!-- Column two stats -->
  <div class="abs stat col-2" style="top:334px">Median Mortgage value<br>of Principal residence<div class="value">$190,000</div></div>
  <div class="abs stat col-2" style="top:422px">Debt to disposable<br>income ratio average<div class="value">172.1</div></div>
  <div class="abs stat col-2" style="top:510px">Total value of all assets<br>held by Canadians in 2016<div class="value wide">12 Trillion dollars</div></div>
  <div class="abs stat col-2" style="top:595px">The principal residence was<br>the single largest asset held<br>(of the 12 Trillion)<div class="value">32%</div></div>
  <div class="abs stat col-2" style="top:693px">Private pensions was the 2nd<br>largest grouping of assets at<div class="value">29.2%</div></div>
  <div class="abs stat col-2" style="top:778px">The average borrowing<br>rate for Canadian mortgages<div class="value">2.94%</div></div>

  <!-- Column three stats -->
  <div class="abs stat col-3" style="top:334px"><em>74%</em> were fixed rate,<br><em>21%</em> were variable<br>and <em>5%</em> blended.</div>
  <div class="abs stat col-3" style="top:403px"><div class="lead">48%</div>of Canadians do not<br>save or invest at all</div>
  <div class="abs stat col-3" style="top:489px"><div class="lead">54%</div>of Canadians do not<br>budget regularly</div>
  <div class="abs stat col-3" style="top:577px"><div class="lead">1 in 3</div>Canadians have lost<br>at least 20% in one year</div>
  <div class="abs stat col-3" style="top:669px"><div class="lead">51%</div>of Canadians took NO ACTION<br>after losing at least 20%<br>in one year.</div>
  <div class="abs stat col-3" style="top:777px"><div class="lead">22%</div>of those people either, hired<br>or fired an advisor</div>

  <h2 class="abs section-label" style="top:874px">Financial advice landscape:</h2>

  <div class="abs icon-fill orange" style="left:74px;top:930px;width:90px;height:46px" role="img" aria-label="Row of houses icon"></div>
  <div class="abs stat col-1" style="top:930px"># of households in Canada<div class="value orange">13,300,000</div></div>

  <div class="abs icon-fill orange" style="left:448px;top:937px;width:40px;height:40px" role="img" aria-label="House icon"></div>
  <div class="abs icon-fill" style="left:488px;top:926px;width:46px;height:52px;background:var(--white)" role="img" aria-label="Advisor figure icon"></div>
  <div class="abs stat col-2" style="top:930px">Households with an advisor<div class="value orange">5,300,000</div></div>

  <svg class="abs" style="left:814px;top:934px" width="40" height="40" viewBox="0 0 40 40" aria-hidden="true">
    <circle cx="20" cy="20" r="17" fill="#fff" stroke="var(--orange)" stroke-width="4"/>
    <text x="20" y="28" font-family="Nunito, sans-serif" font-weight="900" font-size="22" fill="var(--ink)" text-anchor="middle">%</text>
  </svg>
  <div class="abs icon-fill orange" style="left:852px;top:926px;width:50px;height:60px" role="img" aria-label="Advisor figure icon"></div>
  <div class="abs stat col-3" style="top:930px">% of households dissatisfied<br>with existing advisor<div class="value orange">1,100,000</div></div>

  <div class="abs rule rule-bottom"></div>
</div>
</body>
</html>
```